Quillrun Couriers Web design

Take a look at our existing website(www.qlnrun.com) and design a new one, plus coding and recreate an existing logo.

```html
<!DOCTYPE html>
<html lang="en">
<head>
<meta charset="utf-8">
<title>Quillrun Couriers</title>
<link href="https://fonts.googleapis.com/css2?family=Montserrat:wght@400;500;600;700;800&display=swap" rel="stylesheet">
<style>
:root{
  --blue:#1265b4;
  --navy:#0f2f5e;
  --navy-deep:#0b2a57;
  --orange:#ef8a22;
  --ink:#1c1c1c;
  --grey:#666;
  --line:#e4e4e4;
  --sky:#5fb0ff;
}
*{box-sizing:border-box;margin:0;padding:0}
html,body{width:1200px;height:2570px;overflow:hidden}
body{position:relative;font-family:'Montserrat',sans-serif;color:var(--ink);background:#fff}
.abs{position:absolute}
/* header */
.brand{left:88px;top:22px;font-size:20px;font-weight:700;color:var(--blue);display:flex;align-items:center;gap:8px}
.brand-mark{width:16px;height:16px;background:var(--orange)}
.contact-chip{top:20px;display:flex;gap:8px;align-items:center}
.chip-icon{width:28px;height:28px;border:1px solid var(--line);border-radius:3px;display:flex;align-items:center;justify-content:center}
.chip-text small{display:block;font-size:11.5px;color:#333}
.chip-text b{font-size:13px;font-weight:600;color:var(--blue)}
.social{display:flex;gap:8px}
.social span{width:28px;height:28px;border:1px solid var(--line);border-radius:3px;display:block}
.login{left:1012px;top:18px;width:103px;height:33px;background:var(--blue);color:#fff;font-size:12px;font-weight:600;border-radius:3px;display:flex;align-items:center;justify-content:center;gap:5px}
.header-rule{left:88px;top:70px;width:1027px;height:1px;background:var(--line)}
.nav{top:75px;left:197px;display:flex;align-items:center;font-size:13.5px;font-weight:500}
.nav a{color:var(--ink);text-decoration:none;height:31px;line-height:31px;padding:0 20px}
.nav a.active{background:var(--orange);color:#fff;width:82px;text-align:center;padding:0;margin-right:16px}
.nav a+a{margin-right:16px}
/* hero */
.hero{left:0;top:110px;width:1200px;height:468px}
.hero-title{left:107px;top:288px;font-size:46px;font-weight:800;line-height:52px;color:#fff}
.dots{left:1082px;top:525px;display:grid;grid-template-columns:13px 13px;gap:5px}
.dots span{width:13px;height:13px;background:#fff;border-radius:2px}
.dots span.on{background:var(--orange)}
/* sections */
.h2{font-size:32px;font-weight:700;color:var(--blue)}
.body-text{font-size:13.5px;line-height:19.5px;color:#222}
.btn-outline{border:1px solid #222;border-radius:3px;font-size:12px;font-weight:500;display:flex;align-items:center;justify-content:center;background:#fff;color:#222}
.card{top:1209px;width:289px;height:310px;background:#fff;border-radius:6px;padding:40px 31px 0}
.card h3{font-size:21px;font-weight:700;line-height:27px;margin-top:18px;height:58px}
.card p{font-size:13.5px;line-height:18px;color:var(--grey);margin-top:10px;height:72px}
.card .btn-outline{width:108px;height:29px;margin-top:12px;border-color:#999}
.card .btn-fill{background:var(--blue);color:#fff;border-color:var(--blue)}
.benefits{left:693px;top:1773px;list-style:none;font-size:14px;line-height:21px;width:345px}
.benefits li{padding-left:19px;position:relative}
.benefits li::before{content:"";position:absolute;left:0;top:5px;width:9px;height:9px;border:1px solid var(--blue);border-radius:50%}
/* contact */
.contact-head{left:88px;top:2208px;font-size:19px;font-weight:700;color:#fff}
.ci-icon{width:40px;height:40px;border:1.5px solid #fff;border-radius:3px;display:flex;align-items:center;justify-content:center}
.ci-label{font-size:12.5px;color:var(--sky)}
.ci-val{font-size:12.5px;color:#fff;line-height:18px}
.map{left:429px;top:2225px;width:314px;height:244px;border-radius:8px;background:linear-gradient(135deg,#eef2e6,#b9d9b0 55%,#f1ede0)}
.inquiry{left:784px;top:2142px;width:331px;height:375px;background:var(--orange)}
.inquiry h4{position:absolute;top:40px;width:100%;text-align:center;color:#fff;font-size:21px;font-weight:700}
.field{position:absolute;left:33px;width:265px;height:35px;border:1px solid rgba(255,255,255,.55);border-radius:4px;color:#fff;font-size:12px;display:flex;align-items:center;padding-left:12px;gap:7px}
.field.msg{height:60px;align-items:flex-start;padding-top:10px}
.submit{position:absolute;left:33px;top:299px;width:265px;height:36px;background:#fff;border-radius:3px;color:var(--navy);font-size:13px;font-weight:600;display:flex;align-items:center;justify-content:center}
.footer{left:0;top:2517px;width:1200px;height:53px;background:var(--navy-deep)}
.foot-links{left:88px;top:2531px;display:flex;gap:22px;font-size:12.5px;color:#fff}
.copy{left:88px;top:2550px;font-size:12.5px;color:#fff}
.foot-social{left:1012px;top:2534px}
.foot-social span{border-color:#fff;border-radius:3px}
</style>
</head>
<body>

<!-- header -->
<div class="abs brand"><span class="brand-mark"></span>Quillrun Couriers</div>
<div class="abs contact-chip" style="left:537px">
  <div class="chip-icon"><svg width="12" height="12" viewBox="0 0 24 24"><path fill="#1265b4" d="M6.6 10.8a15 15 0 0 0 6.6 6.6l2.2-2.2c.3-.3.7-.4 1-.2 1.1.4 2.3.6 3.6.6.6 0 1 .4 1 1V20c0 .6-.4 1-1 1A17 17 0 0 1 3 4c0-.6.4-1 1-1h3.5c.6 0 1 .4 1 1 0 1.3.2 2.5.6 3.6.1.3 0 .7-.2 1z"/></svg></div>
  <div class="chip-text"><small>Phone</small><b>555-014-7170</b></div>
</div>
<div class="abs contact-chip" style="left:681px">
  <div class="chip-icon"><svg width="13" height="10" viewBox="0 0 26 20"><path fill="#1265b4" d="M0 0h26v20H0z M2 2l11 9 11-9z"/></svg></div>
  <div class="chip-text"><small>Email</small><b>info@qlnrun.com</b></div>
</div>
<div class="abs social" style="left:886px;top:22px"><span></span><span></span><span></span></div>
<div class="abs login"><svg width="10" height="11" viewBox="0 0 10 11"><circle cx="5" cy="3" r="2.6" fill="#fff"/><path d="M0 11c0-3 2-4.5 5-4.5s5 1.5 5 4.5z" fill="#fff"/></svg>Login</div>
<div class="abs header-rule"></div>
<nav class="abs nav">
  <a class="active">Home</a><a>About Us</a><a>Services</a><a>Rates</a><a>Customer Benefits</a><a>Logistics</a><a>Contact Us</a>
</nav>

<!-- hero -->
<svg class="abs hero" viewBox="0 0 1200 468" role="img" aria-label="Photo of two warehouse workers checking a parcel and a tablet, framed by orange and blue diagonal bands">
  <defs>
    <linearGradient id="heroPhoto" x1="0" y1="0" x2="1" y2="1">
      <stop offset="0" stop-color="#c9c4bb"/><stop offset=".5" stop-color="#8ea6c4"/><stop offset="1" stop-color="#4f6e97"/>
    </linearGradient>
  </defs>
  <rect width="1200" height="468" fill="url(#heroPhoto)"/>
  <polygon points="0,0 560,0 240,468 0,468" fill="#1a4f93"/>
  <polygon points="0,90 200,468 0,468" fill="#0a0a0a"/>
  <polygon points="430,0 550,0 210,468 30,468" fill="#ef8a22"/>
  <polygon points="0,0 300,0 120,260 0,90" fill="#ef8a22"/>
  <polygon points="160,0 430,0 130,430 60,280" fill="#1a4f93"/>
  <rect y="464" width="1200" height="4" fill="#1265b4"/>
</svg>
<div class="abs hero-title">We Make Moving<br>Fast &amp; Easy</div>
<div class="abs dots"><span></span><span></span><span class="on"></span><span></span></div>

<!-- about -->
<div class="abs h2" style="left:88px;top:680px">About Us</div>
<div class="abs body-text" style="left:88px;top:738px;width:440px">
  <p>Welcome to Quillrun Couriers. We are committed to providing professional messenger services to cater for the most important, emergency and time sensitive deliveries valuable to your company.</p>
  <p style="margin-top:19px">Our services range from scheduled local and long distance, same day to all types of On Demand services.</p>
  <p style="margin-top:19px">Our goal is to become a leader by showing reliability, integrity as well as competitive pricing....</p>
</div>
<div class="abs btn-outline" style="left:88px;top:941px;width:116px;height:32px">READ MORE</div>
<svg class="abs" style="left:620px;top:620px" width="560" height="400" viewBox="0 0 560 400" role="img" aria-label="Photo of a truck on the road and a courier carrying branded boxes">
  <defs>
    <linearGradient id="aboutPhoto" x1="0" y1="0" x2="0" y2="1">
      <stop offset="0" stop-color="#7fa1c6"/><stop offset=".6" stop-color="#4e6f98"/><stop offset="1" stop-color="#34506f"/>
    </linearGradient>
  </defs>
  <polygon points="14,185 40,185 80,396 50,396" fill="#0f2f5e"/>
  <polygon points="40,96 460,96 460,396 40,396 66,250" fill="url(#aboutPhoto)"/>
  <polygon points="68,96 102,96 40,396 6,396" fill="#ef8a22"/>
  <polygon points="300,70 440,10 480,80 545,230 470,396 230,396 210,180" fill="#d4b28a"/>
</svg>

<!-- services band -->
<svg class="abs" style="left:0;top:1040px" width="1200" height="665" viewBox="0 0 1200 665" role="img" aria-label="Dark blue photo backdrop of a cargo port with containers and a plane">
  <polygon points="0,0 170,72 1055,72 1200,160 1200,662 1040,575 200,575 0,505" fill="#183c6d"/>
  <polygon points="0,0 170,72 1055,72 1200,160 1200,662 1040,575 200,575 0,505" fill="#0f2f5e" opacity=".55"/>
</svg>
<div class="abs card" style="left:120px">
  <svg width="44" height="44" viewBox="0 0 44 44" fill="none" stroke="#ef8a22" stroke-width="2"><rect x="4" y="12" width="36" height="30"/><rect x="14" y="2" width="16" height="12"/><path d="M22 5v6M19 8h6M18 42V32h8v10M9 18h4M9 24h4M31 18h4M31 24h4M18 20h8M18 26h8"/></svg>
  <h3>Hospital &amp;<br>Medical Care</h3>
  <p>Hospital &amp; Medical Care Home Deliveries, Pharmaceuticals and Critical Routes...</p>
  <div class="btn-outline">READ MORE</div>
</div>
<div class="abs card" style="left:457px">
  <svg width="44" height="44" viewBox="0 0 44 44" fill="none" stroke="#ef8a22" stroke-width="2"><path d="M3 14L22 3l19 11zM5 14h34M7 18v16M14 18v16M21 18v16M5 36h28M3 41h30"/><circle cx="35" cy="34" r="7"/><path d="M35 30v8"/></svg>
  <h3>Banking &amp;<br>Brokerage</h3>
  <p>Banking &amp; Brokerage Emergency Deliveries, Mortgage Documents, Interoffice Routes...</p>
  <div class="btn-outline">READ MORE</div>
</div>
<div class="abs card" style="left:794px">
  <svg width="44" height="44" viewBox="0 0 44 44" fill="none" stroke="#ef8a22" stroke-width="2"><path d="M22 3v34M8 8h28M14 40h16M8 8l-6 14h12zM36 8l-6 14h12zM2 22a6 4 0 0 0 12 0M30 22a6 4 0 0 0 12 0"/><circle cx="22" cy="6" r="2"/></svg>
  <h3>Legal Filings</h3>
  <p style="margin-top:-16px;height:98px">Legal, Administrative and also deliveries associated with Manu-facturing. ...</p>
  <div class="btn-outline btn-fill">READ MORE</div>
</div>

<!-- customer benefits -->
<svg class="abs" style="left:88px;top:1712px" width="520" height="345" viewBox="0 0 520 345" role="img" aria-label="Photo of a worker in a safety vest checking a clipboard beside stacked boxes on a pallet">
  <defs>
    <linearGradient id="benPhoto" x1="0" y1="0" x2="1" y2="0">
      <stop offset="0" stop-color="#9fae4a"/><stop offset=".45" stop-color="#c59660"/><stop offset="1" stop-color="#7b5a3a"/>
    </linearGradient>
  </defs>
  <polygon points="0,0 432,0 460,343 0,343" fill="url(#benPhoto)"/>
  <polygon points="436,130 510,130 470,343 437,343" fill="#0f2f5e"/>
  <polygon points="420,40 450,40 516,343 478,343" fill="#ef8a22"/>
</svg>
<div class="abs h2" style="left:693px;top:1720px">Customer&nbsp; Benefits</div>
<ul class="abs benefits">
  <li>Money back guaranteed if your package is not delivered on time</li>
  <li>Free waiting time</li>
  <li>All our services are guaranteed</li>
  <li>Pickup within 15 to 30 mins.of your call or sooner</li>
  <li>First 100lbs. are free</li>
  <li>State of the art courier software system</li>
  <li>Online order entry</li>
  <li>Online order tracking</li>
  <li>Signature capturing</li>
  <li>Be able to see invoices online</li>
  <li>Be able to print shipping labels</li>
</ul>

<!-- contact band -->
<svg class="abs" style="left:0;top:1600px" width="1200" height="920" viewBox="0 0 1200 920">
  <polygon points="1200,0 1200,105 1040,15" fill="#ffffff"/>
  <polygon points="0,455 170,570 1200,570 1200,920 0,920" fill="#163a6a"/>
</svg>
<div class="abs contact-head">Conatct info</div>

<div class="abs ci-icon" style="left:89px;top:2265px"><svg width="14" height="18" viewBox="0 0 14 18"><path d="M7 0a7 7 0 0 0-7 7c0 5 7 11 7 11s7-6 7-11a7 7 0 0 0-7-7z" fill="#fff"/><circle cx="7" cy="7" r="2.6" fill="#163a6a"/></svg></div>
<div class="abs" style="left:145px;top:2257px"><div class="ci-label">Address</div><div class="ci-val">412 Harbor Blvd.<br>Ashford, NY 10420</div></div>
<div class="abs" style="left:266px;top:2257px"><div class="ci-label">Mailing Address</div><div class="ci-val">P.O. Box 5187<br>Ashford, NY 10421</div></div>

<div class="abs ci-icon" style="left:89px;top:2337px"><svg width="15" height="15" viewBox="0 0 24 24"><path fill="#fff" d="M6.6 10.8a15 15 0 0 0 6.6 6.6l2.2-2.2c.3-.3.7-.4 1-.2 1.1.4 2.3.6 3.6.6.6 0 1 .4 1 1V20c0 .6-.4 1-1 1A17 17 0 0 1 3 4c0-.6.4-1 1-1h3.5c.6 0 1 .4 1 1 0 1.3.2 2.5.6 3.6.1.3 0 .7-.2 1z"/></svg></div>
<div class="abs" style="left:145px;top:2341px"><div class="ci-label">Phone</div><div class="ci-val" style="font-weight:600">555-013-2427</div></div>
<div class="abs" style="left:258px;top:2341px"><div class="ci-label">Fax</div><div class="ci-val" style="font-weight:600">555-019-7041</div></div>

<div class="abs ci-icon" style="left:89px;top:2408px"><svg width="16" height="12" viewBox="0 0 26 20"><path fill="#fff" d="M0 0h26v20H0z"/><path d="M1 1l12 10L25 1" stroke="#163a6a" stroke-width="2" fill="none"/></svg></div>
<div class="abs" style="left:145px;top:2412px"><div class="ci-label">Email</div><div class="ci-val" style="font-weight:600">info@qlnrun.com</div></div>

<div class="abs map" role="img" aria-label="Map showing the office location with a pin"></div>

<div class="abs inquiry">
  <h4>Quick Inquiry</h4>
  <div class="field" style="top:83px"><svg width="11" height="12" viewBox="0 0 10 11" fill="none" stroke="#fff"><circle cx="5" cy="3" r="2.5"/><path d="M.5 10.5c0-3 2-4 4.5-4s4.5 1 4.5 4z"/></svg>Name</div>
  <div class="field" style="top:127px"><svg width="8" height="12" viewBox="0 0 8 12" fill="none" stroke="#fff"><rect x=".5" y=".5" width="7" height="11" rx="1"/></svg>Phone</div>
  <div class="field" style="top:171px"><svg width="12" height="9" viewBox="0 0 12 9" fill="none" stroke="#fff"><rect x=".5" y=".5" width="11" height="8"/><path d="M.5.5L6 5l5.5-4.5"/></svg>Email</div>
  <div class="field msg" style="top:215px"><svg width="11" height="11" viewBox="0 0 11 11" fill="none" stroke="#fff"><rect x=".5" y=".5" width="10" height="10" rx="1"/></svg>Message</div>
  <div class="submit">Submit</div>
</div>

<!-- footer -->
<div class="abs footer"></div>
<div class="abs foot-links"><span>Home</span><span>About Us</span><span>Services</span><span>Rates</span><span>Customer Benefits</span><span>Logistics</span><span>Contact Us</span></div>
<div class="abs copy">Copyright © 2021 Ledgerline Web Studio. All Rights Reserved</div>
<div class="abs social foot-social"><span></span><span></span><span></span></div>

</body>
</html>
```